Business Cards for cafe providing speciality coffee and food

I need a business card design for my husband’s businesses. He has two cafes in Brisbane. The business name is Copperleaf Roasting House. They sell high end specialty coffee as well as breakfast and lunch. All the food is cooked fresh, in house and they have strict quality controls for their coffee. I would like the business card to feature the address for both cafes, my husband’s phone number and the business’s instagram. The address for the first is 61 Walden Crescent, Oakvale and the second is 23 Pellow Avenue, Brindlemoor. The Instagram handle is @copperleafroastinghouse and phone number is 0491362847. We already have a business logo that is attached.

Target Market(s)

All ages, higher disposable income and more likely to eat out regularly

Industry/Entity Type

Hospitality

Contact Information for Business Card

Must be suitable for both customers and suppliers

Font styles to use
Sans Serif

Colors

Designer to choose colors to be used in the design.

Requirements
Must have
• Owner’s name: Reid Castell
• Addresses of both cafes: 61 Walden Crescent, Oakvale and 23 Pellow Avenue, Brindlemoor
• Instagram handle: @copperleafroastinghouse
• Contact number: 0491362847
Nice to have
• Business logo

```html
<!DOCTYPE html>
<html lang="en">
<head>
<meta charset="utf-8">
<title>Copperleaf Roasting House – Business Cards</title>
<link href="https://fonts.googleapis.com/css2?family=Lato:wght@400;700&family=Roboto:wght@700&display=swap" rel="stylesheet">
<style>
  :root {
    --backdrop: #6b6b6b;
    --card-white: #ffffff;
    --card-black: #0b0b0b;
    --ink: #111111;
    --ink-soft: #3a3a3a;
    --mark-light: #d9d9d9;
  }
  * { margin: 0; padding: 0; box-sizing: border-box; }
  html, body { width: 1200px; height: 802px; overflow: hidden; }
  body { background: var(--backdrop); position: relative; font-family: "Lato", sans-serif; }

  .card {
    position: absolute;
    top: 274px;
    width: 443px;
    height: 264px;
    overflow: hidden;
  }
  .card--front { left: 136px; background: var(--card-white); }
  .card--back { left: 624px; background: var(--card-black); }

  .front-band {
    position: absolute;
    left: 388px; top: 0;
    width: 55px; height: 100%;
    background: var(--card-black);
  }
  .front-notch {
    position: absolute;
    left: 271px; top: 57px;
    width: 144px; height: 144px;
    border-radius: 50%;
    background: var(--card-white);
  }
  .brand-mark {
    position: absolute;
    display: flex; flex-direction: column; align-items: center; justify-content: center;
    text-align: center;
    font-family: "Lato", sans-serif;
    font-weight: 700;
    text-transform: uppercase;
    letter-spacing: 1px;
    line-height: 1.25;
  }
  .brand-mark--front {
    left: 275px; top: 61px; width: 136px; height: 136px;
    font-size: 12px; color: var(--ink);
  }
  .brand-mark--back {
    left: 151px; top: 62px; width: 140px; height: 140px;
    font-size: 13px; color: var(--mark-light);
  }

  .owner-name {
    position: absolute; left: 24px; top: 74px;
    font-family: "Roboto", sans-serif; font-weight: 700;
    font-size: 16.5px; color: var(--ink); letter-spacing: 0.2px;
  }
  .contact-list { position: absolute; left: 24px; top: 106px; list-style: none; }
  .contact-list li {
    display: flex; align-items: center; gap: 4px;
    font-size: 12.5px; color: var(--ink-soft); height: 16px;
  }
  .contact-icon { width: 13px; height: 13px; flex: none; }
  .address-list { position: absolute; left: 24px; top: 149px; list-style: none; }
  .address-list li { font-size: 13px; color: var(--ink-soft); height: 22px; }
</style>
</head>
<body>

  <section class="card card--front" aria-label="Business card front">
    <div class="front-band"></div>
    <div class="front-notch"></div>

    <h1 class="owner-name">REID CASTELL</h1>

    <ul class="contact-list">
      <li>
        <svg class="contact-icon" viewBox="0 0 16 16" aria-hidden="true">
          <circle cx="8" cy="8" r="8" fill="#111"/>
          <path d="M4 6.2c0-1 1.7-1.8 4-1.8s4 .8 4 1.8v.6h-2v-.8H6v.8H4z M5 8h6l.8 3.5H4.2z" fill="#fff"/>
        </svg>
        0491362847
      </li>
      <li>
        <svg class="contact-icon" viewBox="0 0 16 16" aria-hidden="true">
          <circle cx="8" cy="8" r="8" fill="#111"/>
        </svg>
        @copperleafroastinghouse
      </li>
    </ul>

    <ul class="address-list">
      <li>61 Walden Crescent, Oakvale</li>
      <li>23 Pellow Avenue, Brindlemoor</li>
    </ul>

    <div class="brand-mark brand-mark--front">Copperleaf<br>Roasting<br>House</div>
  </section>

  <section class="card card--back" aria-label="Business card back">
    <div class="brand-mark brand-mark--back">Copperleaf<br>Roasting<br>House</div>
  </section>

</body>
</html>
```